Animal Eye Clinic needs a Business card

We are a new veterinary ophthalmology practice (Tessaly Animal Eye Care) and we need a business card designed. We only see animal eyes - we are not a regular veterinary clinic. We already have a logo. We are looking for a professional, good looking business card to hand out to our clients. We are looking for something simple but professional and contemporary. Our logo is likely the only picture/graphic that needs to be on the card.
Updates

Contact Information for Business Card

Marisol Dunkley, BSc, DVM, MSc, DipACVO
Veterinary Ophthalmologist

Phone: 250.418.3097
Email: tessalyanimaleyecare@mailbrook.net
Website: tessalyanimaleyecare.net
Address: 1840 Pellworth Rd
Kelowna, BC, V4T 8M3

Colors

Designer to choose colors to be used in the design.

Requirements
Must have
• Our logo (attached)

```html
<!DOCTYPE html>
<html lang="en">
<head>
<meta charset="utf-8">
<title>Tessaly Animal Eye Care — Business Card</title>
<link href="https://fonts.googleapis.com/css2?family=Open+Sans:wght@400;600;700&display=swap" rel="stylesheet">
<style>
  :root {
    --bg: #0c0c0c;
    --card: #2a2a2b;
    --teal: #1aa2b3;
    --grey: #8c8c8c;
    --rule: #6a6a6a;
  }
  * { box-sizing: border-box; margin: 0; padding: 0; }
  html, body { width: 1200px; height: 822px; overflow: hidden; }
  body {
    background: var(--bg);
    font-family: "Open Sans", Arial, sans-serif;
    position: relative;
  }
  .card {
    position: absolute;
    top: 268px;
    width: 500px;
    height: 286px;
    background: var(--card);
    border-bottom: 3px solid var(--teal);
    border-left: 1px solid var(--teal);
    box-shadow: 0 20px 40px rgba(0,0,0,.6);
  }
  .card--back { left: 60px; }
  .card--front { left: 640px; }

  /* back side */
  .contact {
    height: 100%;
    display: flex;
    flex-direction: column;
    align-items: center;
    justify-content: center;
    text-align: center;
    color: var(--grey);
  }
  .contact__name {
    color: var(--teal);
    font-weight: 700;
    font-size: 19px;
    letter-spacing: .3px;
    text-transform: uppercase;
  }
  .contact__creds {
    font-weight: 400;
    font-size: 12px;
    margin-left: 4px;
  }
  .contact__title {
    font-size: 10.5px;
    letter-spacing: .6px;
    text-transform: uppercase;
    margin-top: 1px;
  }
  .icon-rule {
    display: flex;
    align-items: center;
    gap: 8px;
    margin: 9px 0 6px;
  }
  .icon-rule__line { width: 90px; height: 1px; background: var(--rule); }
  .icon-rule__icons { display: flex; gap: 3px; }
  .icon { width: 20px; height: 20px; }
  .contact__line {
    font-size: 11.5px;
    letter-spacing: .3px;
    text-transform: uppercase;
    line-height: 1.4;
  }
  .divider { width: 170px; height: 1px; background: var(--rule); margin: 8px 0; }

  /* front side */
  .brand {
    height: 100%;
    display: flex;
    align-items: center;
    justify-content: center;
    gap: 14px;
  }
  .brand__dot {
    width: 46px; height: 46px;
    border-radius: 50%;
    background: var(--teal);
  }
  .brand__name {
    color: var(--teal);
    font-weight: 700;
    font-size: 24px;
    text-transform: uppercase;
    letter-spacing: .4px;
  }
</style>
</head>
<body>

<section class="card card--back" aria-label="Card back: contact details">
  <div class="contact">
    <h1 class="contact__name">Marisol Dunkley<span class="contact__creds">BSc, DVM, MSc, DipACVO</span></h1>
    <p class="contact__title">Veterinary Ophthalmologist</p>

    <div class="icon-rule">
      <span class="icon-rule__line"></span>
      <span class="icon-rule__icons">
        <svg class="icon" viewBox="0 0 20 20" aria-label="Phone"><circle cx="10" cy="10" r="10" fill="#1aa2b3"/><path d="M6.5 5.5c.6-.4 1.2-.3 1.5.2l.9 1.6c.2.4.1.9-.3 1.2l-.6.4c.5 1.2 1.5 2.2 2.7 2.7l.4-.6c.3-.4.8-.5 1.2-.3l1.6.9c.5.3.6.9.2 1.5-.6.9-1.6 1.2-2.6.8-2.6-1-4.6-3-5.6-5.6-.4-1 0-2 .6-2.8z" fill="#2a2a2b"/></svg>
        <svg class="icon" viewBox="0 0 20 20" aria-label="Email"><circle cx="10" cy="10" r="10" fill="#1aa2b3"/><rect x="5" y="6.5" width="10" height="7" rx="1" fill="#2a2a2b"/><path d="M5.5 7l4.5 3.5L14.5 7" stroke="#1aa2b3" stroke-width="1" fill="none"/></svg>
        <svg class="icon" viewBox="0 0 20 20" aria-label="Website"><circle cx="10" cy="10" r="10" fill="#1aa2b3"/><g stroke="#2a2a2b" stroke-width="1.2" fill="none"><circle cx="10" cy="10" r="5"/><ellipse cx="10" cy="10" rx="2.2" ry="5"/><path d="M5 10h10"/></g></svg>
      </span>
      <span class="icon-rule__line"></span>
    </div>

    <p class="contact__line">250.418.3097</p>
    <p class="contact__line">tessalyanimaleyecare@mailbrook.net</p>
    <p class="contact__line">www.tessalyanimaleyecare.net</p>
    <span class="divider"></span>
    <p class="contact__line">1840 Pellworth Rd</p>
    <p class="contact__line">Kelowna, BC, V4T 8M3</p>
  </div>
</section>

<section class="card card--front" aria-label="Card front: practice name">
  <div class="brand">
    <span class="brand__dot"></span>
    <span class="brand__name">Tessaly Animal Eye Care</span>
  </div>
</section>

</body>
</html>
```